Velmora Business Card Design Project

Need a design for Velmora business cards
Square rounded corner card:
http://www.printquilt.example/25-X-25-Rounded-Corner-Business-Cards_p_204.html
Front content (specific example is used to establish format):
Colm Harwick
Founder
650-555-0182
colm@velmora.com
@colmjharwick
www.velmora.com
Back content:
Vertical velmora logo (white on red)
https://www.filecove.example/sh/kq4hlwtnexg31rb/QQWmzr5P714Lk2fJvX3aTnH7c?dl=0
Target Market(s)
Young professionals (early 20's)
Industry/Entity Type
Business
Requirements
Must have
- Look similar to
http://storage.artmarket.example/design_img/413907/52210/52210_9182634_413907_image.jpg
Adapted to square rounded corner format

```html
<!DOCTYPE html>
<html lang="en">
<head>
<meta charset="utf-8">
<title>Velmora Business Card</title>
<link rel="stylesheet" href="https://fonts.googleapis.com/css2?family=Montserrat:wght@400;600;700&display=swap">
<style>
  :root {
    --backdrop: #e2e2e2;
    --card-white: #ffffff;
    --brand-red: #d9261c;
    --ink: #1e1e1e;
    --on-red: #ffffff;
  }
  * { margin: 0; padding: 0; box-sizing: border-box; }
  html, body {
    width: 1200px;
    height: 875px;
    overflow: hidden;
    background: var(--backdrop);
  }
  .canvas {
    position: relative;
    width: 1200px;
    height: 875px;
    font-family: "Montserrat", sans-serif;
  }
  .card {
    position: absolute;
    top: 245px;
    width: 384px;
    height: 384px;
    border-radius: 17px;
    text-align: center;
  }
  .card--contact { left: 191px; background: var(--card-white); color: var(--ink); }
  .card--identity { left: 624px; background: var(--brand-red); color: var(--on-red); }

  .brand-name {
    position: absolute;
    left: 0; right: 0;
    top: 30px;
    font-family: "Montserrat", sans-serif;
    font-weight: 600;
    font-size: 40px;
    line-height: 48px;
    letter-spacing: 1px;
  }
  .card--contact .brand-name { color: var(--brand-red); }
  .card--identity .brand-name { color: var(--on-red); top: 36px; }

  .brand-mark {
    position: absolute;
    left: 50%;
    width: 140px;
    height: 140px;
    margin-left: -70px;
    border-radius: 50%;
  }
  .card--contact .brand-mark { top: 98px; background: var(--brand-red); }
  .card--identity .brand-mark { top: 104px; background: var(--on-red); }

  .contact-list {
    position: absolute;
    left: 0; right: 0;
    top: 272px;
    list-style: none;
    font-size: 16px;
    line-height: 21px;
    font-weight: 400;
  }
  .contact-list .accent { color: var(--brand-red); }

  .person {
    position: absolute;
    left: 0; right: 0;
    top: 302px;
  }
  .person-name { font-weight: 700; font-size: 19px; line-height: 26px; }
  .person-role { font-weight: 400; font-size: 19px; line-height: 26px; }
</style>
</head>
<body>
<main class="canvas">
  <section class="card card--contact">
    <div class="brand-name">velmora</div>
    <div class="brand-mark"></div>
    <ul class="contact-list">
      <li>650-555-0182</li>
      <li>colm@velmora.com</li>
      <li>@colmjharwick</li>
      <li>www.<span class="accent">velmora</span>.com</li>
    </ul>
  </section>

  <section class="card card--identity">
    <div class="brand-name">velmora</div>
    <div class="brand-mark"></div>
    <div class="person">
      <p class="person-name">Colm Harwick</p>
      <p class="person-role">founder</p>
    </div>
  </section>
</main>
</body>
</html>
```